Brivenor Inc. Website

We need a website design for a new company based in Montreal, Canada. Our company offers professional services in planning & scheduling for major construction projects in varying industries. The main colors to be used are black & red (same as in logo). The final design should convey professionalism, precision, and excellence. The following are examples of what the website layout could look like: https://www.quorvalbuild.ca/, https://4671.ca/, https://lumedrix.ca/, https://www.hovtrakemgroup.com/en. Avoid using stock videos or photos with people in it.
Target Market(s)
Target audience are multi-national clients looking to hire a firm to manage their construction projects. Target market is Mining & Metals
Industry/Entity Type
Mining & Metalurgy, Hydroelectricity, Infrastructure
Number of Pages Required
1 page
Colors
Designer to choose colors to be used in the design.
Look and feel
Each slider illustrates characteristics of the customer's brand and the style your logo design should communicate.

```html
<!DOCTYPE html>
<html lang="en">
<head>
<meta charset="utf-8">
<title>Brivenor Inc. — Planning &amp; Scheduling</title>
<link href="https://fonts.googleapis.com/css2?family=Poppins:wght@400;500;600;700&display=swap" rel="stylesheet">
<style>
:root{
  --red:#9b0a1d;
  --red-dark:#4a0610;
  --ink:#1f1f1f;
  --muted:#8a8a8a;
  --light:#f7f7f7;
  --white:#ffffff;
  --line:#e6e6e6;
  --footer:#1e1e1e;
}
*{box-sizing:border-box;margin:0;padding:0}
html,body{width:1200px;height:4177px;overflow:hidden}
body{font-family:'Poppins',sans-serif;color:var(--ink);background:var(--white);position:relative}
.abs{position:absolute}

/* hero */
.hero{position:absolute;left:0;top:0;width:1200px;height:633px;
  background:linear-gradient(180deg,#2b2f35 0%,#4a5058 40%,#5d646b 60%,#2a3138 100%)}
.hero-shade{position:absolute;inset:0;background:linear-gradient(90deg,rgba(0,0,0,.55),rgba(0,0,0,.15))}
.brand{position:absolute;left:109px;top:38px;display:flex;align-items:center;gap:12px;color:var(--white);font-weight:700;font-size:24px;letter-spacing:2px}
.brand-dot{width:34px;height:34px;border-radius:50%;border:3px solid var(--white)}
.nav{position:absolute;top:48px;left:420px;display:flex;gap:0;font-size:13px;color:var(--white)}
.nav a{position:absolute;white-space:nowrap;color:var(--white);text-decoration:none}
.nav-phone{position:absolute;left:874px;top:48px;font-size:13px;color:var(--white)}
.btn-outline{position:absolute;left:978px;top:39px;width:114px;height:41px;border:1.5px solid var(--white);border-radius:3px;color:var(--white);font-size:13px;font-weight:700;display:flex;align-items:center;justify-content:center}
.hero-rule{position:absolute;left:109px;top:215px;width:167px;height:3px;background:var(--white)}
.hero-title{position:absolute;left:109px;top:240px;font-size:55px;line-height:64px;font-weight:700;color:var(--white);text-transform:uppercase}
.hero-sub{position:absolute;left:109px;top:389px;font-size:19px;color:var(--white)}

/* about */
.about{position:absolute;left:0;top:633px;width:1200px;height:970px;background:var(--light)}
.section-title{font-weight:700;font-size:38px;color:var(--ink)}
.about-title{position:absolute;left:109px;top:186px}
.about-text{position:absolute;left:109px;top:253px;width:480px;font-size:13.5px;line-height:19.7px;color:#555}
.about-photo{position:absolute;left:741px;top:76px;width:351px;height:350px;border-radius:6px;
  background:linear-gradient(180deg,#7fb0e0 0%,#cfdde8 35%,#b7bcc0 60%,#6f7479 100%)}
.badge{position:absolute;left:718px;top:303px;width:134px;height:167px;background:var(--white);border-radius:6px;box-shadow:0 6px 20px rgba(0,0,0,.12);text-align:center;font-weight:600;font-size:14px;line-height:22px}
.badge svg{margin-top:20px}
.badge p{margin-top:8px}
.feature{position:absolute;top:575px;width:316px;height:317px;background:var(--white);border-radius:4px;text-align:center;padding-top:70px}
.feature h3{font-size:19px;font-weight:600;line-height:27px;margin-top:18px}
.feature p{font-size:13px;color:var(--muted);line-height:19px;margin:6px auto 0;width:230px}
.feature.active{background:var(--red);color:var(--white)}
.feature.active p{color:#f1c9ce}
.icon-disc{width:66px;height:66px;border-radius:50%;background:var(--white);margin:0 auto;display:flex;align-items:center;justify-content:center}

/* services */
.services{position:absolute;left:0;top:1603px;width:1200px;height:705px;background:var(--white)}
.services-title{position:absolute;left:0;width:1200px;top:75px;text-align:center}
.services-sub{position:absolute;left:0;width:1200px;top:134px;text-align:center;font-size:15px;line-height:22px;color:var(--muted)}
.service-card{position:absolute;top:206px;width:483px;height:422px;border-radius:5px;overflow:hidden}
.service-card .shade{position:absolute;inset:0;background:linear-gradient(180deg,rgba(0,0,0,0) 45%,rgba(0,0,0,.85) 100%)}
.service-card h3{position:absolute;left:40px;top:313px;font-size:19px;font-weight:600;color:var(--white)}
.service-card p{position:absolute;left:40px;top:345px;width:410px;font-size:13px;line-height:19px;color:var(--white)}

/* contact */
.contact{position:absolute;left:0;top:2308px;width:1200px;height:620px;background:linear-gradient(180deg,var(--red) 0%,#6d0814 65%,var(--red-dark) 100%)}
.contact-title{position:absolute;left:0;width:1200px;top:78px;text-align:center;color:var(--white);font-size:38px;font-weight:700;line-height:54px}
.field{position:absolute;color:var(--white);font-size:12px;font-weight:500}
.field .box{margin-top:6px;height:35px;background:var(--white);border-radius:2px;font-size:11px;font-weight:400;color:#aaa;padding:0 10px;display:flex;align-items:center;justify-content:space-between}
.field .box.chosen{color:var(--ink)}
.field .box.tall{height:131px;align-items:flex-start;padding-top:12px}
.submit{position:absolute;left:527px;top:535px;width:145px;height:47px;background:var(--white);border-radius:3px;color:var(--red);font-size:14px;font-weight:700;display:flex;align-items:center;justify-content:center;gap:10px}

.site-photo{position:absolute;left:0;top:2928px;width:1200px;height:381px;
  background:linear-gradient(180deg,#8a6a52 0%,#d9b994 30%,#e3c8a4 60%,#cfae86 100%)}

/* reviews */
.reviews{position:absolute;left:0;top:3309px;width:1200px;height:448px;background:var(--white)}
.reviews-title{position:absolute;left:0;width:1200px;top:80px;text-align:center}
.review{position:absolute;top:160px;width:322px;height:174px;border:1px solid var(--line);padding:18px 20px}
.quote{color:var(--red);font-size:42px;font-weight:700;line-height:34px;height:34px}
.review p{margin-top:10px;font-size:12.5px;line-height:19px;color:var(--muted)}
.review .who{margin-top:16px;font-size:14px;color:var(--ink);font-weight:500}
.dots{position:absolute;top:360px;left:564px;display:flex;gap:11px}
.dots span{width:9px;height:9px;border-radius:50%;background:#d4d4d4}
.dots span.on{background:var(--red)}

/* footer */
.footer{position:absolute;left:0;top:3757px;width:1200px;height:420px;background:var(--footer);color:var(--white)}
.footer-brand{position:absolute;left:113px;top:110px;display:flex;align-items:center;gap:14px;font-size:32px;font-weight:700;letter-spacing:3px}
.footer-brand .brand-dot{width:48px;height:48px;border-width:4px}
.fcol{position:absolute;top:78px}
.fcol h4{font-size:15px;font-weight:500;margin-bottom:16px}
.fcol li{list-style:none;font-size:13px;line-height:26px;display:flex;align-items:center;gap:10px}
.footer-rule{position:absolute;left:109px;top:347px;width:983px;height:1px;background:#555}
.copyright{position:absolute;left:109px;top:378px;font-size:10px;color:#bbb}
.social{position:absolute;top:369px;width:33px;height:32px;background:var(--white);border-radius:3px;display:flex;align-items:center;justify-content:center}
.social span{width:14px;height:14px;border:2px solid var(--red);border-radius:3px}
</style>
</head>
<body>

<header class="hero">
  <div class="hero-shade" role="img" aria-label="Photograph of a modern glass and steel industrial building under a cloudy sky"></div>
  <div class="brand"><span class="brand-dot"></span>BRIVENOR</div>
  <nav class="nav">
    <a style="left:0">About</a>
    <a style="left:68px">Services
      <svg width="10" height="7" viewBox="0 0 10 7" style="margin-left:6px"><path d="M1 1l4 4 4-4" fill="none" stroke="#fff" stroke-width="1.6"/></svg></a>
    <a style="left:174px">Reviews</a>
    <a style="left:256px">Contact</a>
  </nav>
  <div class="nav-phone">+1 514 555 01</div>
  <div class="btn-outline">CONTACT US</div>
  <div class="hero-rule"></div>
  <h1 class="hero-title">Precision Planning<br>for Project Success</h1>
  <p class="hero-sub">Building a Foundation for Seamless Execution and Success</p>
</header>

<section class="about">
  <h2 class="section-title about-title">About Us</h2>
  <p class="about-text">Lorem ipsum dolor sit amet consectetur. Tellus viverra nulla purus amet urna mauris vulputate molestie. Semper arcu tristique aenean diam quisque eget id commodo scelerisque. Leo id est semper aliquet vivamus gravida leo sit vestibulum. Consectetur in diam ut elementum imperdiet. Egestas elit pharetra id enim sit nec eget. Nunc leo pellentesque erat nec aliquam aliquam tortor. Ullamcorper cursus ut feugiat id suspendisse a in.</p>
  <div class="about-photo" role="img" aria-label="Photograph of industrial silos and a processing plant against a blue sky"></div>
  <div class="badge">
    <svg width="44" height="58" viewBox="0 0 44 58" fill="none" stroke="#9b0a1d" stroke-width="1.6">
      <path d="M8 2l2 4 4 .5-3 3 .8 4L8 11.5 4.2 13.5l.8-4-3-3 4-.5z"/>
      <path d="M22 2l2 4 4 .5-3 3 .8 4-3.8-2-3.8 2 .8-4-3-3 4-.5z"/>
      <path d="M36 2l2 4 4 .5-3 3 .8 4-3.8-2-3.8 2 .8-4-3-3 4-.5z"/>
      <path d="M15 17l2 4 4 .5-3 3 .8 4-3.8-2-3.8 2 .8-4-3-3 4-.5z"/>
      <path d="M29 17l2 4 4 .5-3 3 .8 4-3.8-2-3.8 2 .8-4-3-3 4-.5z"/>
      <path d="M19 56V38a3 3 0 016 0v8l6 2v8" stroke="#333"/>
    </svg>
    <p>5 Star<br>Service</p>
  </div>

  <div class="feature active" style="left:109px">
    <div class="icon-disc">
      <svg width="40" height="40" viewBox="0 0 40 40" fill="none" stroke="#9b0a1d" stroke-width="1.6"><circle cx="20" cy="20" r="7"/><circle cx="20" cy="20" r="13" stroke-dasharray="5 3"/><path d="M26 14l8-8M30 6h4v4"/></svg>
    </div>
    <h3>Enhanced Project<br>Efficiency</h3>
    <p>Lorem ipsum dolor sit amet consectetur.</p>
  </div>
  <div class="feature" style="left:442px">
    <div class="icon-disc">
      <svg width="40" height="40" viewBox="0 0 40 40" fill="none" stroke="#555" stroke-width="1.5"><circle cx="20" cy="22" r="12"/><path d="M20 22v-7M20 22l5 3" stroke="#9b0a1d"/><path d="M17 6h6M20 6v4"/></svg>
    </div>
    <h3>Minimized Delays and<br>Disruptions</h3>
    <p>Lorem ipsum dolor sit amet consectetur.</p>
  </div>
  <div class="feature" style="left:776px">
    <div class="icon-disc">
      <svg width="40" height="40" viewBox="0 0 40 40" fill="none" stroke="#555" stroke-width="1.5"><rect x="6" y="8" width="26" height="26"/><rect x="10" y="4" width="26" height="26" stroke="#9b0a1d"/><path d="M15 13l12 12M27 13L15 25" stroke="#9b0a1d"/></svg>
    </div>
    <h3>Maximizing Resource<br>Utilization</h3>
    <p>Lorem ipsum dolor sit amet consectetur.</p>
  </div>
</section>

<section class="services">
  <h2 class="section-title services-title">Our Services</h2>
  <p class="services-sub">Lorem ipsum dolor sit amet consectetur.<br>Tellus viverra nulla purus amet urna mauris vulputate molestie</p>
  <div class="service-card" style="left:109px;background:linear-gradient(135deg,#e9e3da 0%,#c9c2b8 45%,#6b6760 100%)" role="img" aria-label="Photograph of a project planning session over printed charts">
    <div class="shade"></div>
    <h3>Project Management</h3>
    <p>Lorem ipsum dolor sit amet consectetur. Tellus viverra nulla purus amet urna mauris vulputate molestie.</p>
  </div>
  <div class="service-card" style="left:608px;background:linear-gradient(180deg,#b7bdc2 0%,#7d8388 45%,#5b5a4e 75%,#2e2d28 100%)" role="img" aria-label="Photograph of a mining excavator loading a yellow haul truck">
    <div class="shade"></div>
    <h3>Engineering</h3>
    <p>Lorem ipsum dolor sit amet consectetur. Tellus viverra nulla purus amet urna mauris vulputate molestie.</p>
  </div>
</section>

<section class="contact">
  <h2 class="contact-title">Get Ready for an Amazing<br>Transformation! Contact Us Now!</h2>
  <div class="field" style="left:274px;top:215px;width:318px">Name<div class="box">John Doe</div></div>
  <div class="field" style="left:608px;top:215px;width:317px">Phone Number<div class="box">+1 514 5550</div></div>
  <div class="field" style="left:274px;top:286px;width:318px">Email<div class="box">mail@example.com</div></div>
  <div class="field" style="left:608px;top:286px;width:317px">Service<div class="box chosen">Project Management
    <svg width="10" height="7" viewBox="0 0 10 7"><path d="M1 1l4 4 4-4" fill="none" stroke="#333" stroke-width="1.4"/></svg></div></div>
  <div class="field" style="left:274px;top:359px;width:651px">Text Message<div class="box tall">Type your message</div></div>
  <div class="submit">
    <svg width="16" height="16" viewBox="0 0 16 16"><path d="M1 7l14-6-5 14-2-6z" fill="#9b0a1d"/></svg>SUBMIT
  </div>
</section>

<div class="site-photo" role="img" aria-label="Photograph of a yellow backhoe loader digging sand at a construction site"></div>

<section class="reviews">
  <h2 class="section-title reviews-title">Reviews From Our Satisfied Clients</h2>
  <div class="review" style="left:109px">
    <div class="quote">“</div>
    <p>“Lorem ipsum dolor sit consectetur. Unc tellus massa nibh velit pulvinar. Nibh scelerisque at eu potenti scelerisque.”</p>
    <div class="who">Nadia R.</div>
  </div>
  <div class="review" style="left:439px">
    <div class="quote">“</div>
    <p>“Lorem ipsum dolor sit consectetur. Unc tellus massa nibh velit pulvinar. Nibh scelerisque at eu potenti scelerisque.”</p>
    <div class="who">Marc T.</div>
  </div>
  <div class="review" style="left:770px">
    <div class="quote">“</div>
    <p>“Lorem ipsum dolor sit consectetur. Unc tellus massa nibh velit pulvinar. Nibh scelerisque at eu potenti scelerisque.”</p>
    <div class="who">Claire V.</div>
  </div>
  <div class="dots"><span class="on"></span><span></span><span></span><span></span></div>
</section>

<footer class="footer">
  <div class="footer-brand"><span class="brand-dot"></span>BRIVENOR</div>
  <div class="fcol" style="left:608px">
    <h4>Quick Links</h4>
    <ul><li>About</li><li>Services</li><li>Reviews</li><li>Contact</li></ul>
  </div>
  <div class="fcol" style="left:746px">
    <h4>Company</h4>
    <ul><li>Terms and Condition</li><li>Privacy and Plicy</li><li>Career</li></ul>
  </div>
  <div class="fcol" style="left:939px">
    <h4>Contact Us</h4>
    <ul>
      <li><svg width="13" height="13" viewBox="0 0 14 14"><path d="M3 1l2.5 3-1.5 1.5a8 8 0 004.5 4.5L10 8.5l3 2.5-1.5 2.5C6 13 1 8 .8 2.5z" fill="#fff"/></svg>+1 514 55501</li>
      <li><svg width="13" height="10" viewBox="0 0 14 10"><rect width="14" height="10" rx="1" fill="#fff"/><path d="M1 1l6 5 6-5" fill="none" stroke="#1e1e1e" stroke-width="1.3"/></svg>support@brivenor.ca</li>
    </ul>
  </div>
  <div class="footer-rule"></div>
  <div class="copyright">© Brivenor 2023.</div>
  <div class="social" style="left:972px" aria-label="Social link"><span></span></div>
  <div class="social" style="left:1015px" aria-label="Social link"><span></span></div>
  <div class="social" style="left:1059px" aria-label="Social link"><span></span></div>
</footer>

</body>
</html>
```